Electrical Contracting Business Website

Require website done for my contracting business.
Partly done one but really dont have time.

You can view the current one at http://tolbran.net.au

You can use any info/styles/photos from the current website

I like the orange color of the logo so id like things to be with that
Unfortunatly being a new business (Sept 2015) I havent got alot of photos . but if you require any for any of the specifics listed in the doc file ill have a look to see what I have.

I am targeting mainly commercial / industrial clients. Which also includes government and mining.

Target Market(s)

People requiring electricians

Industry/Entity Type

Electrician

Coding

Coded - Design and coding required

Number of Pages Required

5+ page

Colors
f37122

Requirements
Must have
• logo with EC Number
• Keep it simple and not to complicated
• Comply with the current html / style sheet standards.
• Desktop/Mobile Version compatability
Nice to have
• additional photos.
• The domestic lifts we install are by vonrim I dont have any photos of them unfortunately.
Should not have
• change colour of logo

```html
<!DOCTYPE html>
<html lang="en">
<head>
<meta charset="utf-8">
<title>Tolbran Engineering</title>
<link href="https://fonts.googleapis.com/css2?family=Raleway:wght@400;500;600;700&family=Open+Sans:wght@400;600;700&display=swap" rel="stylesheet">
<style>
  :root {
    --orange: #f15a29;
    --orange-brand: #f37122;
    --ink: #1a1a1a;
    --body: #4a4a4a;
    --light: #f3f3f3;
    --rule: #dddddd;
    --footer: #1d2030;
    --button: #55565a;
    --white: #ffffff;
  }
  * { box-sizing: border-box; margin: 0; padding: 0; }
  html, body { width: 1200px; height: 2723px; overflow: hidden; }
  body { position: relative; background: var(--white); font-family: "Open Sans", Arial, sans-serif; color: var(--body); }

  /* Header */
  .site-header { position: absolute; left: 0; top: 0; width: 1200px; height: 149px; background: var(--white); }
  .brand { position: absolute; left: 60px; top: 30px; display: flex; align-items: center; gap: 12px; }
  .brand-mark { width: 44px; height: 44px; border-radius: 50%; background: var(--orange-brand); }
  .brand-name { font-family: "Raleway", Arial, sans-serif; font-weight: 700; font-size: 40px; color: var(--orange-brand); letter-spacing: 1px; text-transform: uppercase; }
  .brand-licence { position: absolute; left: 116px; top: 94px; font-family: "Raleway", Arial, sans-serif; font-size: 9px; font-weight: 700; color: var(--orange-brand); line-height: 12px; }
  .header-email { position: absolute; left: 886px; top: 40px; font-size: 18px; color: #333; }
  .header-call { position: absolute; left: 848px; top: 72px; display: flex; align-items: center; gap: 10px; }
  .call-icon { width: 38px; height: 38px; background: var(--orange); display: flex; align-items: center; justify-content: center; }
  .call-label { font-family: "Raleway", Arial, sans-serif; font-weight: 700; font-size: 20px; color: #333; }
  .call-label span { color: var(--orange); font-weight: 600; }
  .header-rule { position: absolute; left: 848px; top: 113px; width: 280px; height: 1px; background: var(--rule); }

  /* Navigation */
  .main-nav { position: absolute; left: 0; top: 149px; width: 1200px; height: 51px; border-top: 1px solid var(--rule); border-bottom: 4px solid var(--orange); }
  .nav-item { position: absolute; top: 14px; font-family: "Raleway", Arial, sans-serif; font-size: 14px; font-weight: 500; color: #222; letter-spacing: .5px; }
  .nav-item.active { color: var(--orange); }
  .nav-sep { position: absolute; top: 8px; width: 1px; height: 30px; background: #ccc; }

  /* Hero */
  .hero { position: absolute; left: 0; top: 200px; width: 1200px; height: 520px;
    background: linear-gradient(100deg, #5f7a63 0%, #7f9179 12%, #e98a3c 22%, #f07b2a 27%, #d9b39a 34%, #e7e9ec 44%, #c9cfd6 52%, #d9d4bf 62%, #c7a449 72%, #e2c45a 80%, #6b6a52 90%, #3d3f36 100%); }
  .hero-band { position: absolute; left: 0; bottom: 0; width: 100%; height: 48px; background: rgba(40,42,44,.8); }
  .hero-dots { position: absolute; right: 74px; bottom: 16px; display: flex; gap: 6px; }
  .hero-dots i { display: block; width: 14px; height: 14px; background: var(--white); }
  .hero-dots i.on { background: var(--orange); }

  /* Sectors */
  .sectors { position: absolute; left: 0; top: 720px; width: 1200px; height: 556px; background: var(--orange); color: var(--white); }
  .sector { position: absolute; width: 340px; text-align: center; }
  .sector-title { font-family: "Raleway", Arial, sans-serif; font-weight: 600; font-size: 28px; letter-spacing: 1px; }
  .sector-text { font-size: 14px; line-height: 24px; margin-top: 4px; }
  .sector-art { position: absolute; left: 0; top: 164px; }

  /* Provide */
  .provide { position: absolute; left: 0; top: 1276px; width: 1200px; height: 635px; background: var(--white); }
  .provide-frame { position: absolute; left: 67px; top: 114px; width: 272px; height: 396px; border: 7px solid var(--orange); }
  .provide-photo { position: absolute; left: 113px; top: 163px; width: 324px; height: 303px;
    background: linear-gradient(180deg, #707578 0%, #e4d96a 10%, #3f4346 22%, #8e9192 40%, #e7dd74 52%, #3b3f42 66%, #9a9c9c 84%, #6e7273 100%); }
  .provide-title { position: absolute; left: 486px; top: 138px; font-family: "Raleway", Arial, sans-serif; font-weight: 500; font-size: 35px; color: var(--ink); }
  .provide-copy { position: absolute; left: 486px; top: 196px; width: 628px; font-size: 17px; line-height: 30px; color: var(--body); }
  .provide-copy p + p { margin-top: 30px; }

  /* Projects */
  .projects { position: absolute; left: 0; top: 1911px; width: 1200px; height: 478px; background: var(--light); border-top: 1px solid #e2e2e2; }
  .projects-title { position: absolute; left: 0; top: 64px; width: 100%; text-align: center; font-family: "Raleway", Arial, sans-serif; font-weight: 500; font-size: 35px; color: var(--orange); }
  .projects-sub { position: absolute; left: 0; top: 122px; width: 100%; text-align: center; font-size: 17px; color: #444; }
  .project-card { position: absolute; top: 198px; width: 276px; height: 196px; }
  .slider-arrow { position: absolute; top: 278px; width: 31px; height: 40px; background: #111; border-radius: 3px; display: flex; align-items: center; justify-content: center; }

  /* Call to action */
  .cta { position: absolute; left: 0; top: 2389px; width: 1200px; height: 67px; background: var(--orange); }
  .cta-text { position: absolute; left: 93px; top: 19px; font-family: "Raleway", Arial, sans-serif; font-size: 22px; font-weight: 500; color: var(--white); }
  .cta-button { position: absolute; left: 906px; top: 14px; width: 181px; height: 45px; background: var(--button); border-radius: 3px; color: var(--white); font-family: "Raleway", Arial, sans-serif; font-weight: 700; font-size: 18px; display: flex; align-items: center; justify-content: center; gap: 10px; }

  /* Footer */
  .site-footer { position: absolute; left: 0; top: 2456px; width: 1200px; height: 267px; background: var(--footer); color: var(--white); }
  .footer-title { position: absolute; top: 56px; font-family: "Raleway", Arial, sans-serif; font-size: 23px; font-weight: 600; color: var(--orange); }
  .footer-link { position: absolute; font-size: 13px; color: var(--white); }
  .footer-text { position: absolute; font-size: 13px; line-height: 22px; font-weight: 600; color: var(--white); }
  .footer-rule { position: absolute; left: 110px; top: 198px; width: 980px; height: 1px; background: #3a3d4c; }
  .copyright { position: absolute; left: 129px; top: 222px; font-size: 12px; color: #d8d8d8; }
  .partner-badge { position: absolute; left: 840px; top: 210px; width: 120px; height: 44px; background: #4a4d5c; }
  .footer-brand { position: absolute; left: 990px; top: 216px; display: flex; align-items: center; gap: 6px; }
  .footer-brand-mark { width: 16px; height: 16px; border-radius: 50%; background: #8a8d98; }
  .footer-brand-name { font-family: "Raleway", Arial, sans-serif; font-weight: 700; font-size: 20px; color: #8a8d98; text-transform: uppercase; }
</style>
</head>
<body>

<header class="site-header">
  <div class="brand">
    <span class="brand-mark"></span>
    <span class="brand-name">Tolbran</span>
  </div>
  <div class="brand-licence">ACN: 611 402 935<br>ABN: 48 390 671 205 &nbsp; EC LIC: 10473</div>
  <div class="header-email">info@tolbran.net.au</div>
  <div class="header-call">
    <span class="call-icon">
      <svg width="20" height="20" viewBox="0 0 24 24"><path fill="#fff" d="M6.6 10.8c1.4 2.8 3.8 5.1 6.6 6.6l2.2-2.2c.3-.3.7-.4 1-.2 1.1.4 2.3.6 3.6.6.6 0 1 .4 1 1V20c0 .6-.4 1-1 1C10.6 21 3 13.4 3 4c0-.6.4-1 1-1h3.5c.6 0 1 .4 1 1 0 1.3.2 2.5.6 3.6.1.3 0 .7-.2 1z"/></svg>
    </span>
    <span class="call-label">CALL: <span>+61 0400 712 386</span></span>
  </div>
  <div class="header-rule"></div>
</header>

<nav class="main-nav">
  <span class="nav-item active" style="left:84px">HOME</span>
  <span class="nav-sep" style="left:156px"></span>
  <span class="nav-item" style="left:181px">ABOUT US</span>
  <span class="nav-sep" style="left:285px"></span>
  <span class="nav-item" style="left:310px">RESIDENTIAL</span>
  <span class="nav-sep" style="left:436px"></span>
  <span class="nav-item" style="left:461px">COMMERCIAL</span>
  <span class="nav-sep" style="left:586px"></span>
  <span class="nav-item" style="left:615px">INDUSTRIAL</span>
  <span class="nav-sep" style="left:731px"></span>
  <span class="nav-item" style="left:757px">CONTACT US</span>
</nav>

<section class="hero" role="img" aria-label="Electrician in an orange hard hat and safety vest wiring a switchboard full of yellow cables">
  <div class="hero-band"></div>
  <div class="hero-dots"><i></i><i class="on"></i><i></i><i></i></div>
</section>

<section class="sectors">
  <div class="sector" style="left:84px; top:58px">
    <h2 class="sector-title">COMMERCIAL</h2>
    <p class="sector-text">Lorem Ipsum is simply dummy text of the print-<br>ing and typesetting industry.</p>
  </div>
  <div class="sector" style="left:736px; top:58px">
    <h2 class="sector-title">INDUSTRIAL</h2>
    <p class="sector-text">Lorem Ipsum is simply dummy text of the print-<br>ing and typesetting industry.</p>
  </div>
  <div class="sector" style="left:422px; top:406px">
    <h2 class="sector-title">RESIDENTIAL</h2>
    <p class="sector-text">Lorem Ipsum is simply dummy text of the print-<br>ing and typesetting industry.</p>
  </div>
  <svg class="sector-art" width="1200" height="210" viewBox="0 0 1200 210">
    <defs>
      <linearGradient id="commercialTone" x1="0" y1="0" x2="0.3" y2="1">
        <stop offset="0" stop-color="#8ea6c2"/><stop offset=".35" stop-color="#56657d"/><stop offset=".7" stop-color="#2f3646"/><stop offset="1" stop-color="#c98a3e"/>
      </linearGradient>
      <linearGradient id="residentialTone" x1="0" y1="0" x2="0" y2="1">
        <stop offset="0" stop-color="#d9dcdc"/><stop offset=".4" stop-color="#8b8f90"/><stop offset=".75" stop-color="#3e4244"/><stop offset="1" stop-color="#1f2224"/>
      </linearGradient>
      <linearGradient id="industrialTone" x1="0" y1="0" x2="1" y2="1">
        <stop offset="0" stop-color="#c6d3de"/><stop offset=".4" stop-color="#7f96aa"/><stop offset=".7" stop-color="#34495f"/><stop offset="1" stop-color="#1e2b3a"/>
      </linearGradient>
    </defs>
    <g role="img" aria-label="Commercial office building at dusk with lit windows"><polygon points="85,0 416,0 250,205" fill="url(#commercialTone)"/></g>
    <g role="img" aria-label="Residential apartment block with balconies"><polygon points="421,205 587,0 753,205" fill="url(#residentialTone)"/></g>
    <g role="img" aria-label="Engineer inspecting industrial pipework"><polygon points="744,0 1076,0 910,205" fill="url(#industrialTone)"/></g>
  </svg>
</section>

<section class="provide">
  <div class="provide-frame"></div>
  <div class="provide-photo" role="img" aria-label="Rows of circuit breakers with yellow labels in a switchboard"></div>
  <h2 class="provide-title">WHAT &nbsp;DO WE PROVIDE</h2>
  <div class="provide-copy">
    <p>we provide consulting in checking sites &nbsp;with some of the most experienced engineers and architects. we have been in service from past 15 years and providing &nbsp;simply dummy text of the printing and typesetting industry. Lorem Ipsum has been the industry's standard dummy text ever since the 1500s, when an unknown</p>
    <p>Printer took a galley of type and scrambled it to make a type specimen book. It has survived not only five centuries, but also the leap into electronic typesetting, remaining essentially unchanged.</p>
  </div>
</section>

<section class="projects">
  <h2 class="projects-title">RECENT PROJECTS</h2>
  <p class="projects-sub">we provide consulting in checking sites &nbsp;with some of the most experienced engineers</p>
  <div class="slider-arrow" style="left:65px">
    <svg width="14" height="18" viewBox="0 0 14 18"><path d="M10 2 L3 9 L10 16" stroke="#fff" stroke-width="2.5" fill="none"/></svg>
  </div>
  <div class="project-card" style="left:151px; background:linear-gradient(100deg,#3b4148 0%,#e9ebe8 25%,#d8dcd6 45%,#8fbf4a 62%,#e8eae4 78%,#59606a 100%)" role="img" aria-label="Circuit breaker and contactor modules on a DIN rail"></div>
  <div class="project-card" style="left:463px; background:linear-gradient(160deg,#b7b2a2 0%,#5d605b 30%,#26292a 55%,#6d6f68 78%,#c4bda9 100%)" role="img" aria-label="Electric motor installed on site"></div>
  <div class="project-card" style="left:775px; background:linear-gradient(180deg,#7a7e80 0%,#e4d96a 14%,#3f4346 28%,#8e9192 48%,#e3d76e 60%,#3b3f42 75%,#9a9c9c 100%)" role="img" aria-label="Completed switchboard with labelled breakers"></div>
  <div class="slider-arrow" style="left:1104px">
    <svg width="14" height="18" viewBox="0 0 14 18"><path d="M4 2 L11 9 L4 16" stroke="#fff" stroke-width="2.5" fill="none"/></svg>
  </div>
</section>

<section class="cta">
  <p class="cta-text">If You Need Any Industrial Solution ... We Are Available For You</p>
  <div class="cta-button">CONTACT US
    <svg width="12" height="16" viewBox="0 0 12 16"><path d="M3 2 L9 8 L3 14" stroke="#fff" stroke-width="2.5" fill="none"/></svg>
  </div>
</section>

<footer class="site-footer">
  <h3 class="footer-title" style="left:125px">Navigation Links</h3>
  <span class="footer-link" style="left:125px; top:100px">Home</span>
  <span class="footer-link" style="left:125px; top:129px">About Us</span>
  <span class="footer-link" style="left:125px; top:158px">Residential</span>
  <span class="footer-link" style="left:307px; top:100px">Commercial</span>
  <span class="footer-link" style="left:307px; top:129px">Industrial</span>
  <span class="footer-link" style="left:307px; top:158px">Contact Us</span>

  <h3 class="footer-title" style="left:490px; top:52px">Specifications</h3>
  <p class="footer-text" style="left:490px; top:95px; width:300px">Delivering unbeatable electrical services.</p>
  <p class="footer-text" style="left:490px; top:138px; width:300px">Contact us now to find out how we can help you with your next electrical solution.</p>

  <h3 class="footer-title" style="left:833px">Contact Us</h3>
  <p class="footer-text" style="left:833px; top:96px; width:340px">Tel : +61 0400 712 386<br>Fax : +61 (08) 6100 4827<br>E-mail : info@tolbran.net.au<br>Harlow Ridge, Western Australia, 6059.</p>

  <div class="footer-rule"></div>
  <p class="copyright">Copyright © 2016 Tolbran Engineering Pty Ltd All Rights Reserved EC 10473</p>
  <div class="partner-badge" role="img" aria-label="Industry association member badge"></div>
  <div class="footer-brand">
    <span class="footer-brand-mark"></span>
    <span class="footer-brand-name">Tolbran</span>
  </div>
</footer>

</body>
</html>
```